Fold out sales presenter

Looking for an A4 single or double fold sales presenter to help staff in a golf pro shop communicate the USPs of our hero products and other one other products.
All the information is available on one webpage.
https://brindlewedge.com/pages/putter-technology
I will upload photos which would be good if they could be edited to have the same background and lighting.
The branding is black white and red as per the website.

With thanks,
Gareth

```html
<!DOCTYPE html>
<html lang="en">
<head>
<meta charset="utf-8">
<title>Brindlewedge Putter Technology – Sales Presenter</title>
<link href="https://fonts.googleapis.com/css2?family=Poppins:ital,wght@0,400;0,500;0,600;0,700;0,800;1,800;1,900&family=Roboto+Condensed:wght@500;600&display=swap" rel="stylesheet">
<style>
:root{
  --stage:#9e9e9e;
  --ink:#0b0b0c;
  --ink-soft:#1d1d1f;
  --white:#ffffff;
  --muted:#d6d6d6;
  --red:#e3262b;
  --rule:#6b6b6b;
}
*{margin:0;padding:0;box-sizing:border-box}
html,body{width:1200px;height:862px;overflow:hidden;background:var(--stage)}
body{position:relative;font-family:"Poppins",sans-serif;color:var(--white)}
.page{position:absolute;top:88px;width:485px;height:686px;background:radial-gradient(ellipse at 50% 45%,#2a2a2c 0%,var(--ink) 70%);overflow:hidden}
.page--cover{left:97px}
.page--range{left:618px}
.abs{position:absolute}
.photo{position:absolute;border-radius:4px}
.wordmark{font-weight:800;color:var(--white);letter-spacing:.5px;line-height:1}
.headline{font-weight:900;font-style:italic;text-transform:uppercase;line-height:1}
.accent{color:var(--red)}
.red-dash{position:absolute;height:2px;width:26px;background:var(--red)}
.tick-list{list-style:none}
.tick-list li{display:flex;align-items:center;gap:7px}
.tick{flex:none;border-radius:50%;background:var(--red);display:inline-flex;align-items:center;justify-content:center}
.small-copy{font-size:7px;line-height:10.5px;color:var(--muted)}
.footer{position:absolute;left:0;right:0;top:645px;height:18px}
.footer .bar{position:absolute;top:6px;height:5px;background:var(--red);width:152px}
.footer .bar--l{left:0}.footer .bar--r{right:0}
.footer .url{position:absolute;left:0;right:0;text-align:center;font-size:17px;font-weight:800;font-style:italic;line-height:18px}

/* cover */
.tagline{left:321px;top:39px;font-size:13px;font-weight:700;display:flex;align-items:center;gap:4px}
.tagline .tag{background:var(--red);padding:1px 5px;transform:skewX(-12deg);display:inline-block}
.tagline .tag span{display:inline-block;transform:skewX(12deg)}
.hero-title{left:0;right:0;top:129px;text-align:center;font-size:36px}
.hero-list{left:235px;top:219px;font-size:13.5px;font-weight:500}
.hero-list li{height:23px}
.why-title{left:34px;top:383px;font-size:21px}
.why{left:34px;top:418px;width:162px}
.why-item{border-top:1px solid var(--rule);height:49px;padding-top:4px}
.why-item:last-child{border-bottom:1px solid var(--rule)}
.why-item h3{font-size:10.5px;font-weight:700;line-height:13px}
.why-item p{font-size:7px;line-height:9.8px;color:var(--muted);margin-top:1px}
.made-in{left:310px;width:170px;top:574px;text-align:center;font-family:"Roboto Condensed",sans-serif;font-weight:500;font-size:15.5px;line-height:14.5px;text-transform:uppercase}

/* range */
.product-name{left:0;right:0;top:54px;text-align:center;font-size:24px}
.built{left:34px;top:104px;font-size:20px;font-weight:800;font-style:italic;line-height:23px}
.section-label{font-family:"Roboto Condensed",sans-serif;font-weight:500;text-transform:uppercase}
.benefits-title{left:275px;top:111px;font-size:15px}
.benefits{left:275px;top:131px;font-size:8.5px}
.benefits li{height:17.2px}
.face-rule{left:34px;right:34px;top:258px;display:flex;align-items:center;gap:8px}
.face-rule .line{flex:1;height:1px;background:var(--rule)}
.face-rule span{font-size:9.5px;letter-spacing:4px;font-weight:500}
.option h2{font-size:18px;font-weight:800;font-style:italic;text-transform:uppercase;line-height:20px}
.option h4{font-size:12px;font-weight:500;line-height:15px;margin-top:2px}
.option ul{list-style:none;margin-top:4px}
.option li{font-size:6.8px;line-height:9.8px;color:var(--muted);padding-left:7px;position:relative}
.option li::before{content:"";position:absolute;left:0;top:4px;width:2.5px;height:2.5px;border-radius:50%;background:var(--red)}
.option p{font-size:7px;line-height:10.5px;color:var(--muted);margin-top:4px}
.divider{left:34px;right:34px;top:510px;height:1px;background:var(--rule)}
</style>
</head>
<body>

<!-- Cover page -->
<section class="page page--cover">
  <div class="abs wordmark" style="left:33px;top:38px;font-size:21px">BRINDLEWEDGE</div>
  <div class="abs tagline">Putter <span class="tag"><span>Technology</span></span></div>

  <div class="red-dash" style="left:229px;top:113px"></div>
  <h1 class="abs headline hero-title">See the line.<br>Trust the stroke.</h1>

  <div class="photo" role="img" aria-label="Studio photo of a carbon putter head viewed from behind" style="left:50px;top:205px;width:155px;height:145px;background:radial-gradient(ellipse at 50% 55%,#5b5b5e 0%,#2b2b2d 45%,transparent 72%)"></div>

  <ul class="abs tick-list hero-list">
    <li><span class="tick" style="width:14px;height:14px"><svg width="8" height="8" viewBox="0 0 10 10"><path d="M2 5.2 4.2 7.4 8.2 2.8" fill="none" stroke="#fff" stroke-width="1.8"/></svg></span>Precision Alignment</li>
    <li><span class="tick" style="width:14px;height:14px"><svg width="8" height="8" viewBox="0 0 10 10"><path d="M2 5.2 4.2 7.4 8.2 2.8" fill="none" stroke="#fff" stroke-width="1.8"/></svg></span>Exceptional Stability</li>
    <li><span class="tick" style="width:14px;height:14px"><svg width="8" height="8" viewBox="0 0 10 10"><path d="M2 5.2 4.2 7.4 8.2 2.8" fill="none" stroke="#fff" stroke-width="1.8"/></svg></span>Consistent Roll</li>
  </ul>
  <p class="abs small-copy" style="left:234px;top:302px;width:220px">Brindlewedge Putters combine advanced carbon composite construction, precision alignment technology and custom fitting to help golfers start more putts on line and control distance with confidence. Even on off-centre strikes</p>

  <div class="photo" role="img" aria-label="Close-up photo of a carbon mallet putter with a milled copper face and shaft" style="left:205px;top:330px;width:280px;height:290px;background:radial-gradient(ellipse at 55% 60%,#55555a 0%,#35332f 35%,rgba(140,90,50,.25) 50%,transparent 72%)"></div>

  <h2 class="abs headline why-title" style="text-transform:none">Why <span class="accent">Brindlewedge?</span></h2>
  <div class="abs why">
    <div class="why-item"><h3>Alignment Confidence</h3><p>Developed with optometrist input to help golfers aim more accurately.</p></div>
    <div class="why-item"><h3>Extreme Stability</h3><p>Carbon composite construction allows weight to be positioned where it maximises forgiveness.</p></div>
    <div class="why-item"><h3>Consistent Roll</h3><p>Engineered to promote predictable launch characteristics and improved distance control.</p></div>
    <div class="why-item"><h3>Custom Fitting</h3><p>Length, loft, lie, swing weight and grip options tailored to each golfer.</p></div>
  </div>

  <div class="abs made-in">Designed &amp;<br>Manufactured in<br>Australia</div>

  <div class="footer"><div class="bar bar--l"></div><div class="url">brindlewedge.com</div><div class="bar bar--r"></div></div>
</section>

<!-- Range page -->
<section class="page page--range">
  <div class="photo" role="img" aria-label="Dimly lit photo of several carbon putter heads grouped together" style="left:150px;top:0;width:335px;height:250px;background:radial-gradient(ellipse at 60% 45%,#3a3a3c 0%,#222224 45%,transparent 75%)"></div>

  <div class="abs wordmark" style="right:34px;top:40px;font-size:11px">BRINDLEWEDGE</div>
  <h1 class="abs headline product-name">Talon RS Carbon</h1>
  <div class="red-dash" style="left:229px;top:85px"></div>

  <h2 class="abs built">Built to Perform<br>When Every Putt<br>Matters</h2>
  <p class="abs small-copy" style="left:34px;top:183px;width:202px">The Talon RS is engineered to maximise stability through advanced carbon composite construction and perimeter weighting, helping golfers maintain speed and direction on off-centre strikes.</p>

  <div class="abs section-label benefits-title">Key Benefits</div>
  <ul class="abs tick-list benefits">
    <li><span class="tick" style="width:9px;height:9px"><svg width="6" height="6" viewBox="0 0 10 10"><path d="M2 5.2 4.2 7.4 8.2 2.8" fill="none" stroke="#fff" stroke-width="2"/></svg></span>Precision Alignment Technology</li>
    <li><span class="tick" style="width:9px;height:9px"><svg width="6" height="6" viewBox="0 0 10 10"><path d="M2 5.2 4.2 7.4 8.2 2.8" fill="none" stroke="#fff" stroke-width="2"/></svg></span>High-MOI Stability</li>
    <li><span class="tick" style="width:9px;height:9px"><svg width="6" height="6" viewBox="0 0 10 10"><path d="M2 5.2 4.2 7.4 8.2 2.8" fill="none" stroke="#fff" stroke-width="2"/></svg></span>Consistent Roll &amp; Distance Control</li>
    <li><span class="tick" style="width:9px;height:9px"><svg width="6" height="6" viewBox="0 0 10 10"><path d="M2 5.2 4.2 7.4 8.2 2.8" fill="none" stroke="#fff" stroke-width="2"/></svg></span>Fully Custom Fitted</li>
    <li><span class="tick" style="width:9px;height:9px"><svg width="6" height="6" viewBox="0 0 10 10"><path d="M2 5.2 4.2 7.4 8.2 2.8" fill="none" stroke="#fff" stroke-width="2"/></svg></span>Designed &amp; Manufactured in Australia</li>
  </ul>

  <div class="abs face-rule"><div class="line"></div><span>FACE OPTIONS</span><div class="line"></div></div>

  <div class="photo" role="img" aria-label="Photo of putter head with a white soft face insert" style="left:20px;top:270px;width:160px;height:115px;background:radial-gradient(ellipse at 50% 55%,#6a6a6d 0%,#303032 45%,transparent 72%)"></div>
  <div class="abs option" style="left:198px;top:286px;width:250px">
    <h2>Soft <span class="accent">Slate 27</span></h2>
    <h4>Maximum Forward Roll Performance</h4>
    <ul>
      <li>Promotes the most forward roll of any Brindlewedge face option</li>
      <li>Reduces initial skid for earlier true roll</li>
      <li>Delivers a consistent, predictable roll across varying green speeds</li>
    </ul>
  </div>

  <div class="abs option" style="left:35px;top:391px;width:250px">
    <h2>Milled <span class="accent">Copper Face</span></h2>
    <h4>Traditional Feel. Premium Feedback.</h4>
    <ul>
      <li>Precision milled copper face</li>
      <li>Soft, responsive impact sensation</li>
      <li>Exceptional feedback and touch</li>
      <li>Strong forward-roll characteristics with a traditional feel</li>
    </ul>
  </div>
  <div class="photo" role="img" aria-label="Photo of putter head with a milled copper face" style="left:285px;top:378px;width:170px;height:125px;background:radial-gradient(ellipse at 50% 60%,#5e5a55 0%,rgba(150,100,60,.45) 35%,#2a2a2c 55%,transparent 75%)"></div>

  <div class="abs divider"></div>

  <div class="photo" role="img" aria-label="Photo of compact carbon blade putter seen from above" style="left:50px;top:525px;width:120px;height:115px;background:radial-gradient(ellipse at 50% 50%,#5c5c60 0%,#2c2c2e 50%,transparent 75%)"></div>
  <div class="abs option" style="left:198px;top:540px;width:260px">
    <h2>Brindlewedge <span class="accent">EL</span></h2>
    <h4>Compact Profile. Exceptional Stability.</h4>
    <p>Designed for golfers who demand precision and consistency, the Brindlewedge EL combines carbon composite construction, precision weighting and advanced alignment features in a confidence-inspiring package.</p>
  </div>

  <div class="footer"><div class="bar bar--l"></div><div class="url">brindlewedge.com</div><div class="bar bar--r"></div></div>
</section>

</body>
</html>
```